Hip and quirky Indian restaurant Menu

We need a build your own bowl/meal/wrap menu similar to Verdigo others. We would like illustrations if possible of India/veggies/chicken/animals/themes. Please utilize the colors that match the schema of the logos provided. We have included pictures you may use them if you would like to. Menu provided is our old menu.

Target Market(s)

Millenials, Ge

Industry/Entity Type

Retail

Font styles to use
Sans Serif
Decorative

Requirements
Must have
• logical placements for build your own meal options
Nice to have
• Illustrations.

```html
<!DOCTYPE html>
<html lang="en">
<head>
<meta charset="utf-8">
<title>Curry Lane – Restaurant Menu</title>
<link href="https://fonts.googleapis.com/css2?family=Anton&family=Kaushan+Script&family=Montserrat:wght@500;800&display=swap" rel="stylesheet">
<style>
:root{
  --orange:#f26424;
  --ribbon:#ef6a3a;
  --navy:#2b2866;
  --ink:#1f1a17;
  --paper:#ffffff;
  --peach:#fde0b8;
  --watermark:#ececec;
}
*{margin:0;padding:0;box-sizing:border-box}
html,body{width:842px;height:1200px;overflow:hidden;background:var(--paper)}
.menu{position:relative;width:842px;height:1200px;background:var(--paper);color:var(--ink);font-family:"Montserrat",sans-serif}
.abs{position:absolute}

/* header */
.title-script{left:22px;top:22px;font-family:"Kaushan Script",cursive;font-size:60px;line-height:1;color:var(--ink)}
.title-block{left:30px;top:86px;font-family:"Anton",sans-serif;font-size:160px;line-height:1;letter-spacing:2px;color:#2a2523}
.tagline{left:96px;top:204px;width:212px;height:42px;background:var(--ribbon);transform:rotate(-8deg);
  clip-path:polygon(0 0,100% 0,94% 50%,100% 100%,0 100%,6% 50%);
  font-family:"Kaushan Script",cursive;font-size:22px;color:#fff;display:flex;align-items:center;justify-content:center}

/* section banners */
.banner{display:flex;align-items:center;justify-content:center;gap:14px;color:#fff;
  font-family:"Kaushan Script",cursive;
  clip-path:polygon(0 4%,20% 0,45% 5%,70% 0,100% 3%,99% 30%,100% 60%,99% 100%,70% 96%,40% 100%,15% 95%,0 100%,1% 60%,0 30%)}
.banner--orange{background:var(--orange)}
.banner--navy{background:var(--navy)}
.banner .icon{width:30px;height:30px;border:2px solid #fff;border-radius:6px;flex:none}
.banner-build{left:29px;top:252px;width:364px;height:70px;font-size:34px}
.banner-lassi{left:31px;top:678px;width:362px;height:67px;font-size:32px}
.banner-fries{left:29px;top:1004px;width:364px;height:68px;font-size:36px}
.banner-chicken{left:429px;top:233px;width:368px;height:71px;font-size:38px}
.banner-snacks{left:417px;top:425px;width:388px;height:73px;font-size:40px}
.banner-dessert{left:417px;top:679px;width:388px;height:73px;font-size:40px}
.banner-drinks{left:417px;top:820px;width:388px;height:74px;font-size:40px}

/* build your own */
.step{left:33px;width:357px}
.step-head{display:flex;justify-content:space-between;align-items:baseline}
.step-name{font-weight:800;line-height:1}
.step-desc{font-weight:500;font-size:12.3px;line-height:16.4px;margin-top:4px}
.price{font-family:"Kaushan Script",cursive;font-weight:400;line-height:1}
.step .price{font-size:30px}
.watermark{left:110px;top:395px;width:250px;height:225px;border-radius:50%;background:var(--watermark);opacity:.45}

/* rows */
.row{display:flex;justify-content:space-between;align-items:baseline;font-weight:800;line-height:1}
.row .price{font-size:19px}
.lassi-row{left:33px;width:356px;font-size:16px}
.lassi-row .pair{display:flex;gap:14px}
.lassi-row .pair .price{width:48px;text-align:right}
.size-row{left:33px;width:356px;font-size:17px}
.size-row .size-label{width:270px;text-align:center;padding-left:40px}
.size-row .pair{display:flex;gap:14px}
.size-row .pair span{width:48px;text-align:center}
.fries-row{left:29px;width:360px;font-size:16.5px}
.chicken-row{left:440px;width:362px;font-size:16px}
.chicken-row .price{font-size:20px}

/* orange column */
.column{left:417px;top:425px;width:388px;height:754px;background:var(--orange);
  clip-path:polygon(0 0,100% 0,100% 90%,98% 96%,95% 91%,92% 100%,86% 93%,80% 99%,72% 92%,65% 98%,58% 93%,50% 100%,42% 93%,35% 98%,27% 92%,20% 99%,12% 93%,6% 97%,0 92%)}
.col-row{color:var(--navy);font-size:16.5px}
.col-row .price{font-size:20px;color:var(--navy)}
.snack-row{left:430px;width:367px}
.drink-row{left:431px;width:357px}

/* brand */
.brand-art{left:522px;top:42px;width:190px;height:190px;border-radius:50%;background:var(--peach);opacity:.75}
.brand-name{left:490px;top:112px;width:270px;text-align:center;font-family:"Montserrat",sans-serif;font-weight:800;font-size:44px;line-height:1;color:var(--navy)}
</style>
</head>
<body>
<div class="menu">

  <div class="abs title-script">Restaurant</div>
  <div class="abs title-block">MENU</div>
  <div class="abs tagline">Tagline Here</div>

  <div class="abs brand-art" role="img" aria-label="Soft mandala flower pattern behind the restaurant name"></div>
  <div class="abs brand-name">Curry Lane</div>

  <!-- Build your own -->
  <div class="abs banner banner--orange banner-build"><span class="icon" role="img" aria-label="Sandwich icon"></span>Build Your Own Meal</div>
  <div class="abs watermark" role="img" aria-label="Faint burger illustration"></div>

  <div class="abs step" style="top:334px">
    <div class="step-head"><span class="step-name" style="font-size:21px">PICK BOWL/WRAP</span><span class="price">$8.00</span></div>
    <p class="step-desc">Salad Bowl, Basmati Rice Bowl, Curry Rice Bowl,<br>Paratha Wrap</p>
  </div>
  <div class="abs step" style="top:404px">
    <div class="step-head"><span class="step-name" style="font-size:16px">PICK MAIN CURRY OPTION</span><span class="price">$8.00</span></div>
    <p class="step-desc">Veg Korma, Chana Masala, CTM, Chili Chicken, Tandoori<br>Chicken, Beef Curry +$1, Goat Curry $2) Double Protein<br>$2 *(For premium curryextra)</p>
  </div>
  <div class="abs step" style="top:492px">
    <div class="step-head"><span class="step-name" style="font-size:21px">PICK TOPPINGS</span><span class="price">$8.00</span></div>
    <p class="step-desc">BeetsThoran, Green BeansThoran, Cabbage<br>Thoran, Chick Pea Salad,Cucumber Salad,diced<br>Onion, chopped bell pepper, shredded Cheese,<br>cilantro, jalapeno</p>
  </div>
  <div class="abs step" style="top:600px">
    <div class="step-head"><span class="step-name" style="font-size:16px">PICK SAUCES</span><span class="price">$8.00</span></div>
    <p class="step-desc">Original Mint, Sweet Tamarind, Cool Yogurt,<br>Mango Chilli, Tikka Masala</p>
  </div>

  <!-- Lassi -->
  <div class="abs banner banner--orange banner-lassi"><span class="icon" role="img" aria-label="Cocktail glass icon"></span>Lassi/ Indian Shakes</div>
  <div class="abs row size-row" style="top:757px"><span class="size-label">SIZE</span><span class="pair"><span>S</span><span>L</span></span></div>
  <div class="abs row lassi-row" style="top:786px"><span>ORIGINAL LASSI</span><span class="pair"><span class="price">$2.00</span><span class="price">$2.50</span></span></div>
  <div class="abs row lassi-row" style="top:824px"><span>PICK MAIN CURRY OPTION</span><span class="pair"><span class="price">$2.50</span><span class="price">$3.00</span></span></div>
  <div class="abs row lassi-row" style="top:860px"><span>PICK TOPPINGS</span><span class="pair"><span class="price">$2.50</span><span class="price">$3.00</span></span></div>
  <div class="abs row lassi-row" style="top:896px"><span>PICK SAUCES</span><span class="pair"><span class="price">$2.75</span><span class="price">$3.25</span></span></div>
  <div class="abs row lassi-row" style="top:933px"><span>PICK TOPPINGS</span><span class="pair"><span class="price">$2.75</span><span class="price">$3.25</span></span></div>
  <div class="abs row lassi-row" style="top:969px"><span>PICK SAUCES</span><span class="pair"><span class="price">$2.75</span><span class="price">$3.25</span></span></div>

  <!-- Loaded fries -->
  <div class="abs banner banner--orange banner-fries"><span class="icon" role="img" aria-label="Fries box icon"></span>Loaded Fries</div>
  <div class="abs row fries-row" style="top:1087px"><span>CHICKEN TIKKA FRIES</span><span class="price">$6.00</span></div>
  <div class="abs row fries-row" style="top:1126px"><span>TANDOORI FRIES</span><span class="price">$6.00</span></div>
  <div class="abs row fries-row" style="top:1162px"><span>CHILI CHICKEN FRIES</span><span class="price">$6.00</span></div>

  <!-- Chicken meals -->
  <div class="abs banner banner--orange banner-chicken"><span class="icon" role="img" aria-label="Chicken drumstick icon"></span>Chicken Meals</div>
  <div class="abs row chicken-row" style="top:321px"><span>TANDOORI CHICKEN /FRIES</span><span class="price">$7.00</span></div>
  <div class="abs row chicken-row" style="top:360px"><span>CHICKEN TENDER/ FRIES</span><span class="price">$7.00</span></div>
  <div class="abs row chicken-row" style="top:396px"><span>SPICY CHICKEN TENDER/ FRIES</span><span class="price">$7.00</span></div>

  <!-- Orange column -->
  <div class="abs column"></div>

  <div class="abs banner banner--navy banner-snacks"><span class="icon" role="img" aria-label="Donut icon"></span>Snacks</div>
  <div class="abs row col-row snack-row" style="top:504px"><span>SAMOSA</span><span class="price">$1.00</span></div>
  <div class="abs row col-row snack-row" style="top:532px"><span>VEG PUFFS</span><span class="price">$1.49</span></div>
  <div class="abs row col-row snack-row" style="top:560px"><span>EGG PUFFS</span><span class="price">$2.49</span></div>
  <div class="abs row col-row snack-row" style="top:589px"><span>SWEET PUFFS</span><span class="price">$1.49</span></div>
  <div class="abs row col-row snack-row" style="top:618px"><span>BEEF PUFFS</span><span class="price">$1.49</span></div>
  <div class="abs row col-row snack-row" style="top:646px"><span>CHICKEN PUFFS</span><span class="price">$1.49</span></div>

  <div class="abs banner banner--navy banner-dessert"><span class="icon" role="img" aria-label="Egg cup icon"></span>Dessert</div>
  <div class="abs row col-row snack-row" style="top:764px"><span>MANGO PUDDING</span><span class="price">$3.50</span></div>
  <div class="abs row col-row snack-row" style="top:791px"><span>RICE PUDDING</span><span class="price">$3.50</span></div>

  <div class="abs banner banner--navy banner-drinks"><span class="icon" role="img" aria-label="Drink glass icon"></span>Drinks</div>
  <div class="abs row col-row drink-row" style="top:912px"><span>ICED TEA 32OZ</span><span class="price">$2.00</span></div>
  <div class="abs row col-row drink-row" style="top:951px"><span>LEMONADE 32OZ</span><span class="price">$2.00</span></div>
  <div class="abs row col-row drink-row" style="top:987px"><span>MASALA TEA</span><span class="price">$2.00</span></div>
  <div class="abs row col-row drink-row" style="top:1024px"><span>INDIAN COFFEE</span><span class="price">$2.00</span></div>
  <div class="abs row col-row drink-row" style="top:1061px"><span>SODA CAN</span><span class="price">$1.00</span></div>
  <div class="abs row col-row drink-row" style="top:1098px"><span>WATER BOTTLE</span><span class="price">$1.00</span></div>

</div>
</body>
</html>
```